" Soluçoes de tecnologia focadas em impressao e outsourcing de impressao visando a reduçao de custos de impressao e a melhoria de processos para pequenas, médias e grandes empresas corporativas e governo através de licitações. Atendimento ao público(balcão) com soluções de grafica rápida, impressão de dados variáveis, impressão de provas de consursos Gerenciar e racionalizar os processos de impressao/cópia através de uso inteligente de tecnologia de última geraçao. Contabilizar páginas/cópias impressas, gerenciar suprimentos. Otimizar processos internos para cada departamento e necessidade. Solução de digitalização de documentos. "

```html
<!DOCTYPE html>
<html lang="pt-BR">
<head>
<meta charset="UTF-8">
<title>Tipora — Soluções que impressionam</title>
<link href="https://fonts.googleapis.com/css2?family=Roboto+Condensed:wght@300;400;700&display=swap" rel="stylesheet">
<style>
  :root {
    --page-bg: #eceeef;
    --screen-bg: #ffffff;
    --brand-red: #e3302b;
    --ink-dark: #2a2a2a;
    --hero-top: #8a8680;
    --hero-mid: #a59c91;
    --hero-warm: #c88a4f;
    --hero-deep: #5d4a3c;
    --white: #ffffff;
    --avatar: #d9a27c;
  }
  * { margin: 0; padding: 0; box-sizing: border-box; }
  html, body {
    width: 1200px; height: 1200px; overflow: hidden;
    background: var(--page-bg);
    font-family: "Roboto Condensed", Arial, sans-serif;
  }
  .mobile-screen {
    position: absolute; left: 320px; top: 30px;
    width: 560px; height: 1140px;
    background: var(--screen-bg);
    border-radius: 36px;
    overflow: hidden;
    box-shadow: 0 10px 40px rgba(0,0,0,0.12);
  }
  .site-header {
    height: 130px;
    display: flex; align-items: center; justify-content: center;
    position: relative;
  }
  .brand {
    display: flex; align-items: center; gap: 10px;
    font-weight: 700; font-size: 34px; color: var(--ink-dark);
    letter-spacing: 0.5px;
  }
  .brand-mark { width: 26px; height: 26px; background: var(--brand-red); }
  .menu-toggle { position: absolute; right: 34px; top: 50%; transform: translateY(-50%); }
  .hero {
    position: relative; height: 1010px;
  }
  .hero-photo {
    position: absolute; inset: 0;
    background:
      linear-gradient(180deg, rgba(0,0,0,0) 55%, rgba(0,0,0,0.45) 100%),
      linear-gradient(170deg, var(--hero-top) 0%, var(--hero-mid) 38%, var(--hero-warm) 70%, var(--hero-deep) 100%);
  }
  .hero-title {
    position: absolute; left: 0; right: 0; top: 600px;
    text-align: center; color: var(--white);
    line-height: 1;
  }
  .hero-title .line-light {
    display: block; font-weight: 300; font-size: 58px; letter-spacing: 3px;
  }
  .hero-title .line-bold {
    display: block; font-weight: 700; font-size: 64px; letter-spacing: 1px; margin-top: 6px;
  }
  .slider-dots {
    position: absolute; bottom: 40px; left: 0; right: 0;
    display: flex; justify-content: center; gap: 22px;
  }
  .slider-dots span {
    width: 20px; height: 20px; border-radius: 50%;
    border: 3px solid var(--white);
  }
  .slider-dots span.is-active { background: var(--white); }
  .support-tab {
    position: absolute; right: 0; top: 190px;
    width: 64px; height: 230px;
    background: var(--brand-red);
    border-radius: 16px 0 0 16px;
    display: flex; flex-direction: column; align-items: center;
    padding-top: 12px; gap: 14px;
  }
  .support-avatar {
    width: 42px; height: 42px; border-radius: 50%;
    background: var(--avatar); border: 3px solid var(--white);
  }
  .support-label {
    writing-mode: vertical-rl; transform: rotate(180deg);
    color: var(--white); font-size: 22px; font-weight: 400;
  }
  .support-label b { font-weight: 700; }
</style>
</head>
<body>
  <main class="mobile-screen">
    <header class="site-header">
      <div class="brand"><span class="brand-mark"></span>Tipora</div>
      <svg class="menu-toggle" width="38" height="30" viewBox="0 0 38 30" aria-label="Menu">
        <rect x="0" y="0" width="38" height="4" fill="var(--brand-red)"/>
        <rect x="10" y="13" width="28" height="4" fill="var(--brand-red)"/>
        <rect x="4" y="26" width="34" height="4" fill="var(--brand-red)"/>
      </svg>
    </header>
    <section class="hero">
      <div class="hero-photo" role="img" aria-label="Foto de escritório com equipe trabalhando em uma mesa com notebook e amostras de cores"></div>
      <h1 class="hero-title">
        <span class="line-light">SOLUÇÕES QUE</span>
        <span class="line-bold">IMPRESSIONAM</span>
      </h1>
      <div class="slider-dots"><span></span><span class="is-active"></span><span></span></div>
      <aside class="support-tab">
        <div class="support-avatar" role="img" aria-label="Foto da atendente"></div>
        <div class="support-label">Suporte <b>Online</b></div>
      </aside>
    </section>
  </main>
</body>
</html>
```